Valtor Word Documentation Template

Create word documentation template for Valtor. This should include cover page, table of contect, list of tables, different style heading etc. The template needs to be inline with valtor.com.au website in terms of colors and style, needs to be clean and simple. We are providing professional services in technology sector. The final design should communicate clean, professional and modern approach

Industry/Entity Type

It Professional

```html
<!DOCTYPE html>
<html lang="en">
<head>
<meta charset="utf-8">
<title>Valtor Document Template</title>
<link rel="stylesheet" href="https://fonts.googleapis.com/css2?family=Fira+Sans:wght@400;500;600&family=Arimo:wght@400&display=swap">
<style>
:root{
  --orange:#ec9148;
  --orange-text:#e8762c;
  --ink:#111111;
  --grey-text:#6f6f6f;
  --row-grey:#f2f2f2;
  --rule:#333333;
  --backdrop:#e6e8eb;
  --paper:#ffffff;
  --footer-band:#f1f2f2;
}
*{box-sizing:border-box;margin:0;padding:0}
html,body{width:1010px;height:1200px;overflow:hidden;background:var(--backdrop)}
.page{position:absolute;left:154px;top:100px;width:691px;height:995px;background:var(--paper);box-shadow:0 0 6px rgba(0,0,0,.25);font-family:"Fira Sans",sans-serif}
.page-header{position:absolute;left:0;top:0;width:100%;height:81px;border-bottom:1px solid #ececec}
.brand{position:absolute;left:50px;top:22px;display:flex;align-items:center;gap:8px}
.brand-dot{width:30px;height:30px;border-radius:50%;background:var(--orange)}
.brand-name{font-size:32px;font-weight:500;color:var(--orange);letter-spacing:.5px}
.brand-tagline{position:absolute;left:88px;top:56px;font-size:6px;color:var(--orange);letter-spacing:1px}
.contact{position:absolute;right:26px;top:20px;text-align:right;font-family:"Arimo",sans-serif;font-size:11px;line-height:12px;color:var(--grey-text)}
.contact-line{display:flex;justify-content:flex-end;align-items:center;gap:4px}
.contact-icon{width:9px;height:9px;display:inline-block}
.doc-table{position:absolute;left:77px;width:537px;border-collapse:collapse;table-layout:fixed;font-size:12px}
.doc-table td{border:1px solid var(--rule);text-align:center;color:var(--ink);height:32px}
.doc-table .head{background:var(--orange);font-weight:600}
.doc-table .bold{font-weight:600}
.doc-table .accent{color:var(--orange-text)}
.doc-table .shaded td:not(.head){background:var(--row-grey)}
.table-a{top:111px}
.table-b{top:196px}
.table-c{top:352px}
.heading{position:absolute;left:83px;font-weight:600;color:var(--ink);white-space:nowrap}
.heading.orange{color:var(--orange-text)}
.h1{font-size:17px}
.h2,.h3,.h4{font-size:15px}
.h5{font-size:12px}
.page-footer{position:absolute;left:0;bottom:0;width:100%;height:34px;background:var(--footer-band);text-align:center;line-height:34px;font-size:12px;color:var(--grey-text)}
</style>
</head>
<body>
<div class="page">
  <header class="page-header">
    <div class="brand"><span class="brand-dot"></span><span class="brand-name">Valtor</span></div>
    <div class="brand-tagline">technology solutions</div>
    <div class="contact">
      <div class="contact-line">Suite 210, 48 Harbour Lane, Sydney <svg class="contact-icon" viewBox="0 0 10 10"><path d="M1 5 5 1 9 5V9H1Z" fill="#ec9148"/></svg></div>
      <div class="contact-line" style="margin-right:13px">NSW, 2000, Australia</div>
      <div class="contact-line">1300 555 017 <svg class="contact-icon" viewBox="0 0 10 10"><path d="M2 1 4 3 3 4Q4 6 6 7L7 6 9 8 8 9Q3 8 1 2Z" fill="#ec9148"/></svg></div>
      <div class="contact-line">info@valtor.com.au <svg class="contact-icon" style="width:13px" viewBox="0 0 13 10"><rect x="1" y="2" width="11" height="7" fill="#ec9148"/><path d="M1 2 6.5 6 12 2" stroke="#fff" fill="none"/></svg> www.valtor.com.au <svg class="contact-icon" viewBox="0 0 10 10"><circle cx="5" cy="5" r="4.5" fill="#ec9148"/></svg></div>
    </div>
  </header>

  <table class="doc-table table-a">
    <tr><td class="head">Table Text</td><td class="head">Table Text</td><td class="head">Table Text</td><td class="head">Table Text</td><td class="head">Table Text</td><td class="head">Table Text</td></tr>
    <tr><td>Table Text</td><td>Table Text</td><td>Table Text</td><td>Table Text</td><td>Table Text</td><td>Table Text</td></tr>
  </table>

  <table class="doc-table table-b">
    <tr><td class="head">Table Text</td><td class="head">Table Text</td><td class="head">Table Text</td><td class="head">Table Text</td><td class="head">Table Text</td><td class="head">Table Text</td></tr>
    <tr><td class="head" style="font-weight:400">Table Text</td><td>Table Text</td><td>Table Text</td><td>Table Text</td><td>Table Text</td><td>Table Text</td></tr>
    <tr class="shaded"><td class="head" style="font-weight:400">Table Text</td><td class="accent">Table Text</td><td class="accent">Table Text</td><td class="accent">Table Text</td><td class="accent">Table Text</td><td class="accent">Table Text</td></tr>
    <tr><td class="head" style="font-weight:400">Table Text</td><td>Table Text</td><td>Table Text</td><td>Table Text</td><td>Table Text</td><td>Table Text</td></tr>
  </table>

  <table class="doc-table table-c">
    <tr><td class="head">Table Text</td><td class="bold">Table Text</td><td class="bold">Table Text</td><td class="bold">Table Text</td><td class="bold">Table Text</td><td class="bold">Table Text</td></tr>
    <tr><td class="head">Table Text</td><td class="accent">Table Text</td><td class="accent">Table Text</td><td class="accent">Table Text</td><td class="accent">Table Text</td><td class="accent">Table Text</td></tr>
    <tr class="shaded"><td class="head">Table Text</td><td>Table Text</td><td>Table Text</td><td>Table Text</td><td>Table Text</td><td>Table Text</td></tr>
    <tr><td class="head">Table Text</td><td>Table Text</td><td>Table Text</td><td>Table Text</td><td>Table Text</td><td>Table Text</td></tr>
  </table>

  <h1 class="heading h1" style="top:534px">Heading 1 - New Page, Biggest</h1>
  <h2 class="heading h2" style="top:569px">Heading 2 - Graduating Smaller</h2>
  <h3 class="heading h3" style="top:601px">Heading 3 - Graduating Smaller</h3>
  <h4 class="heading h4" style="top:633px">Heading 4 - Graduating Smaller</h4>
  <h5 class="heading h5" style="top:663px">Heading 5 - Just Bold</h5>

  <h1 class="heading orange h1" style="top:738px">Heading 1 - New Page, Biggest</h1>
  <h2 class="heading orange h2" style="top:773px">Heading 2 - Graduating Smaller</h2>
  <h3 class="heading orange h3" style="top:805px">Heading 3 - Graduating Smaller</h3>
  <h4 class="heading orange h4" style="top:837px">Heading 4 - Graduating Smaller</h4>
  <h5 class="heading orange h5" style="top:868px">Heading 5 - Just Bold</h5>

  <footer class="page-footer">Page 1 to 30</footer>
</div>
</body>
</html>
```